Security Guard company needs new procedure template to wow potential clients in tender submissions

We need an update to our procedure template that will look very professional and modern. We have many procedures so this template must be editable so the content can be adjusted by us depending on the procedure.
A smart and modern professional front page with editable title etc.
A professional and modern page template for the body of the procedure.

We wish to copy and paste our word document onto this template and be able to use it easily.

I have attached our logo and example of a procedure we have.

Font styles to use
Sans Serif

Requirements
Must have
• Ability for me to edit text and add new sections to the document.
Use as a template for multiple procedures.

```html
<!DOCTYPE html>
<html lang="en">
<head>
<meta charset="utf-8">
<title>Northgate Guarding Limited – HSE Plan</title>
<link href="https://fonts.googleapis.com/css2?family=Montserrat:wght@500;700;800&family=Open+Sans:wght@400;600&display=swap" rel="stylesheet">
<style>
  :root{
    --backdrop:#e6e7ea;
    --page:#ffffff;
    --brand-red:#a3212e;
    --band:#dcdee3;
    --band-light:#eceef1;
    --ink:#34363d;
    --ink-soft:#5a5d66;
    --frame:#1d1d21;
  }
  *{box-sizing:border-box;margin:0;padding:0}
  html,body{width:1200px;height:789px;overflow:hidden}
  body{background:var(--backdrop);font-family:"Open Sans",Arial,sans-serif;color:var(--ink);position:relative}
  .page{position:absolute;top:28px;width:530px;height:733px;background:var(--page);box-shadow:0 2px 10px rgba(0,0,0,.12)}
  .page--contents{left:65px;padding:34px 44px}
  .page--body{left:605px;padding:10px}
  .page--body .frame{border:6px solid var(--frame);height:100%;padding:18px 20px}

  /* brand */
  .brand{display:flex;align-items:center;justify-content:center;gap:12px;margin-bottom:26px}
  .brand__mark{width:22px;height:22px;background:var(--ink)}
  .brand__name{font-family:"Montserrat",Arial,sans-serif;font-weight:700;font-size:22px;color:var(--ink);line-height:1}

  /* contents */
  .contents__title{background:var(--band);font-family:"Montserrat",Arial,sans-serif;font-weight:800;color:var(--brand-red);font-size:15px;letter-spacing:1.5px;text-align:center;padding:8px 0;margin-bottom:10px;border-radius:3px}
  .contents__list{list-style:none}
  .contents__item{display:flex;align-items:center;height:30px;padding:0 12px;font-size:12.5px;border-radius:3px}
  .contents__item:nth-child(odd){background:var(--band-light)}
  .contents__item:nth-child(even){background:var(--band)}
  .contents__num{width:34px;color:var(--ink-soft);font-weight:600}
  .contents__label{flex:1}
  .contents__page{color:var(--ink-soft)}

  /* body sections */
  .section{margin-bottom:12px}
  .section__head{background:var(--brand-red);color:#fff;font-family:"Montserrat",Arial,sans-serif;font-weight:700;font-size:14px;letter-spacing:.5px;padding:5px 10px;margin-bottom:7px;clip-path:polygon(0 0,100% 0,97% 100%,0 100%)}
  .section__lead{font-size:11px;font-weight:600;margin-bottom:4px;line-height:1.4}
  .section p{font-size:10.5px;line-height:1.45}
  .ticks{list-style:none;margin:3px 0 4px}
  .ticks li{position:relative;padding-left:16px;font-size:10px;line-height:1.42;margin-bottom:2px}
  .ticks li::before{content:"\2605";position:absolute;left:2px;top:0;color:var(--brand-red);font-size:9px}
  .role{margin-bottom:6px}
  .role__head{background:var(--band);font-family:"Montserrat",Arial,sans-serif;font-weight:700;font-size:11.5px;padding:4px 10px;margin-bottom:4px;border-left:4px solid var(--brand-red)}
  .role p{font-size:10px;line-height:1.4;padding:0 2px}
</style>
</head>
<body>

<section class="page page--contents">
  <header class="brand">
    <span class="brand__mark"></span>
    <span class="brand__name">Northgate Guarding Limited</span>
  </header>
  <h1 class="contents__title">TABLE OF CONTENTS</h1>
  <ol class="contents__list">
    <li class="contents__item"><span class="contents__num">01</span><span class="contents__label">Purpose</span><span class="contents__page">02</span></li>
    <li class="contents__item"><span class="contents__num">02</span><span class="contents__label">Scope</span><span class="contents__page">02</span></li>
    <li class="contents__item"><span class="contents__num">03</span><span class="contents__label">Responsibilities</span><span class="contents__page">02</span></li>
    <li class="contents__item"><span class="contents__num">04</span><span class="contents__label">HSE Management System</span><span class="contents__page">03</span></li>
    <li class="contents__item"><span class="contents__num">05</span><span class="contents__label">NGL HSE Core Values</span><span class="contents__page">03</span></li>
    <li class="contents__item"><span class="contents__num">06</span><span class="contents__label">NGL HSE Policy Statement</span><span class="contents__page">05</span></li>
    <li class="contents__item"><span class="contents__num">07</span><span class="contents__label">NGL HSE Policy Commitments</span><span class="contents__page">06</span></li>
    <li class="contents__item"><span class="contents__num">08</span><span class="contents__label">Accidents</span><span class="contents__page">06</span></li>
    <li class="contents__item"><span class="contents__num">09</span><span class="contents__label">Consultation</span><span class="contents__page">06</span></li>
    <li class="contents__item"><span class="contents__num">10</span><span class="contents__label">Fire</span><span class="contents__page">07</span></li>
    <li class="contents__item"><span class="contents__num">11</span><span class="contents__label">Personal Protective Equipment</span><span class="contents__page">08</span></li>
    <li class="contents__item"><span class="contents__num">12</span><span class="contents__label">Housekeeping</span><span class="contents__page">08</span></li>
    <li class="contents__item"><span class="contents__num">13</span><span class="contents__label">Waste Disposal</span><span class="contents__page">09</span></li>
    <li class="contents__item"><span class="contents__num">14</span><span class="contents__label">Monitoring</span><span class="contents__page">09</span></li>
    <li class="contents__item"><span class="contents__num">15</span><span class="contents__label">Training</span><span class="contents__page">10</span></li>
    <li class="contents__item"><span class="contents__num">16</span><span class="contents__label">Fit to Work Policy</span><span class="contents__page">10</span></li>
    <li class="contents__item"><span class="contents__num">17</span><span class="contents__label">Drug and Alcohol Policy</span><span class="contents__page">11</span></li>
  </ol>
</section>

<section class="page page--body">
  <div class="frame">
    <article class="section">
      <h2 class="section__head">1. PURPOSE</h2>
      <p class="section__lead">The purpose of this Health and Safety (HSE) Plan is to:</p>
      <ul class="ticks">
        <li>Provide a statement of the Northgate Guarding Limited (NGL) commitment to health and safety performance and how this will be achieved.</li>
        <li>Establish the health and safety objectives, targets, key performance indicators, supervision, audits and communication activities.</li>
      </ul>
    </article>

    <article class="section">
      <h2 class="section__head">2. SCOPE</h2>
      <p>This annual Health and Safety plan is issued as a part of the NGL Health and Safety Management System. This plan covers all activities undertaken by NGL.</p>
    </article>

    <article class="section">
      <h2 class="section__head">3. Responsibilities</h2>
      <div class="role">
        <h3 class="role__head">Owner</h3>
        <p>The Owner of the HSE Plan is the Director, who has the collective responsibility for:</p>
        <ul class="ticks">
          <li>Leading and endorsing the HSE Plan.</li>
          <li>Ensuring that resources are available to execute the HSE Plan.</li>
          <li>Monitoring implementation of the HSE Plan and initiating corrective action where necessary.</li>
        </ul>
      </div>
      <div class="role">
        <h3 class="role__head">Custodian</h3>
        <p>The custodian of the plan is the Operations Manager who has the responsibility for:</p>
        <ul class="ticks">
          <li>Developing the plan.</li>
          <li>Briefing the plan.</li>
          <li>Tracking status of implementation of the HSE Plan and the need for adjustments.</li>
          <li>Ensuring that staff and employees understand their duties and procedures.</li>
        </ul>
      </div>
      <div class="role">
        <h3 class="role__head">Implementation</h3>
        <p>The implementation of the plan are the Supervisors who have the responsibility for:</p>
        <ul class="ticks">
          <li>Carrying out site inspections and reporting findings.</li>
          <li>Ensuring risk assessments, method statements and emergency procedures are current at assignment locations.</li>
        </ul>
      </div>
    </article>
  </div>
</section>

</body>
</html>
```